Visitenkarten für Familienunternehmen in den Bereichen Fliesen, Natursteine, Kaminöfen, Schwimmbäder und Whirlpools
Zielgruppe
Wir sind ein Familienunternehmen in dritter Generation und Spezialist für Fliesen, Natursteine, Kaminöfen, Schwimmbäder und Whirlpools. Professionell, kreativ und voller Leidenschaft begleiten wir unsere Kunden bei der Umsetzung ihrer Vorhaben. Von der persönlichen Beratung bis hin zur Ausführung profitieren unsere Kunden von qualifiziertem Fachpersonal und 60 Jahren Erfahrung. Unsere Zielgruppe sind Familien/Paare ab 35 Jahren, die Produkte höchster Qualität für Ihr Zuhause suchen.
Aufgabenstellung
Wir benötigen neue Visitenkarten, da wir ein neues Logo haben. Wir haben folgende Vorstellung:
Rückseite: Komplett schwarz bzw. dunkel (Farbton ähnlich DB703), mittig unser neues Logo in weiß.
Vorderseite: Auch hier Hintergrund schwarz, Logo in weiß, Name des Ansprechpartners samt Titel/Position, Firmenname, Adresse, Telefonnummer, eMail-Adresse und Social Media-Adresse. Des Weiteren sollte unser Portfolio aufgelistet sein (Fliesen, Natursteine, Kaminöfen, Schwimmbäder und Whirlpools). Alternativ können wir uns die Auflistung des Portfolios auch auf der Rückseite vorstellen. Alternativ können wir uns die Vorderseite auch in weiß mit schwarzer Schrift vorstellen.
Der Inhalt der Datei, welche am Ende erstellt wird, muss für unsere Druckerei editierbar sein (Schrift als Text, nicht als Pfad).
Ergänzung 25.03.2023:
Nachdem die ersten Design-Vorschläge eingetroffen sind, haben wir uns dazu entschieden, dass es eine Visitenkarte im Querformat sein soll. Vorder- und Rückseite vollen schwarz/dunkel sein.

```html
<!DOCTYPE html>
<html lang="de">
<head>
<meta charset="utf-8">
<title>Marmor Tamebrok – Visitenkarten</title>
<link rel="stylesheet" href="https://fonts.googleapis.com/css2?family=Figtree:wght@300;400;700&display=swap">
<style>
  :root {
    --stage: #a68862;
    --card: #3a3635;
    --white: #ffffff;
    --gold: #c9a06a;
    --rule: #8a8584;
  }
  * { margin: 0; padding: 0; box-sizing: border-box; }
  html, body { width: 1200px; height: 846px; overflow: hidden; }
  body {
    position: relative;
    background: var(--stage);
    font-family: "Figtree", Arial, sans-serif;
    color: var(--white);
  }
  .card {
    position: absolute;
    width: 488px;
    height: 316px;
    background: var(--card);
  }
  .card--back { left: 246px; top: 82px; }
  .card--front { left: 550px; top: 437px; }

  .wordmark {
    font-weight: 300;
    color: var(--white);
    text-transform: uppercase;
    white-space: nowrap;
  }
  .card--back .wordmark {
    position: absolute;
    left: 0; right: 0; top: 124px;
    text-align: center;
    font-size: 44px;
    letter-spacing: 0.2em;
    padding-left: 0.2em;
  }
  .card--front .wordmark {
    position: absolute;
    right: 44px; top: 50px;
    font-size: 24px;
    letter-spacing: 0.16em;
  }

  .company {
    position: absolute;
    left: 50px; top: 62px;
    font-size: 13px;
    font-weight: 700;
    letter-spacing: 0.02em;
    color: var(--gold);
    text-transform: uppercase;
  }
  .contact {
    position: absolute;
    left: 50px; top: 121px;
    font-size: 14px;
    line-height: 20px;
    font-weight: 400;
  }
  .contact p { white-space: nowrap; }
  .contact .gap { margin-top: 12px; }
  .contact strong { font-weight: 700; }
  .contact .label { display: inline-block; width: 40px; }
  .social { display: flex; align-items: center; gap: 8px; }
  .social-dot { width: 12px; height: 12px; border-radius: 50%; background: var(--white); margin-right: 8px; margin-left: 1px; }

  .divider {
    position: absolute;
    left: 300px; top: 109px;
    width: 1px; height: 156px;
    background: var(--rule);
  }
  .portfolio {
    position: absolute;
    left: 329px; top: 167px;
    list-style: none;
    font-size: 13.5px;
    line-height: 20.5px;
    color: var(--gold);
    text-transform: uppercase;
    letter-spacing: 0.01em;
  }
</style>
</head>
<body>
  <section class="card card--back" aria-label="Rückseite">
    <div class="wordmark">Tamebrok</div>
  </section>

  <section class="card card--front" aria-label="Vorderseite">
    <div class="company">Marmor Tamebrok GmbH</div>
    <div class="wordmark">Tamebrok</div>

    <div class="contact">
      <p><strong>Timo Tamebrok</strong> | Geschäftsführer</p>
      <p>Lindenweg 7 | 76812 Altdorf</p>
      <p class="gap"><span class="label">Tel. :</span> +49 (0) 06 31 2 - 48 48 00</p>
      <p class="gap"><span class="label">Mail:</span> info@marmor-tamebrok.de</p>
      <p><span class="label">Web:</span> www.marmor-tamebrok.de</p>
      <p class="social"><span class="social-dot" aria-hidden="true"></span>@marmortamebrok</p>
    </div>

    <div class="divider" aria-hidden="true"></div>

    <ul class="portfolio">
      <li>Fliesen</li>
      <li>Natursteine</li>
      <li>Kaminöfen</li>
      <li>Schwimmbäder</li>
      <li>Whirlpools</li>
    </ul>
  </section>
</body>
</html>
```